Co-Living Retreat Centre Pitch Deck

We are needing fresh new pitch deck for our Co-Living Retreat Centre project. We are building a 40 unit community focused on personal development and holistic living!

Here is the branding guide:
https://www.plorvex.com/sheet/QWRT8mHkzp3/vbLoPnXaTd_4uR-7eWsMqY/open

Here is the Content:
https://files.tamberlo.com/store/boxes/8K4Pm2vRtXw7nQ91bLzHyE5cJd3sFa0Gq?mode=viewing

Target Market(s)

30-45 Year olds that are into Yoga, Meditation, Personal Development, Balance Lifestyle.

Font styles to use
Serif
Sans Serif

Requirements
Must have
• Must have the colours from our branding.
Nice to have
• Have some elements of nature, Inspiration,

```html
<!DOCTYPE html>
<html lang="en">
<head>
<meta charset="utf-8">
<title>The Verdant – Co-Living Retreat Pitch Deck</title>
<link href="https://fonts.googleapis.com/css2?family=DM+Serif+Display&family=Inter:wght@400;500;600;700&display=swap" rel="stylesheet">
<style>
  :root{
    --page:#f2f2f2;
    --sage:#77906f;
    --sage-deep:#5f7b57;
    --cream:#efeed9;
    --cream-soft:#e6e8d2;
    --forest:#2d4a26;
    --ink:#2b3326;
    --white:#ffffff;
    --serif:'DM Serif Display', Georgia, serif;
    --sans:'Inter', Arial, sans-serif;
  }
  *{box-sizing:border-box;margin:0;padding:0}
  html,body{width:960px;height:1200px;overflow:hidden;background:var(--page)}
  body{position:relative;font-family:var(--sans);color:var(--ink)}
  .slide{position:absolute;width:415px;height:233px;overflow:hidden;box-shadow:0 1px 3px rgba(0,0,0,.12)}
  .col-l{left:51px}.col-r{left:502px}
  .row-1{top:69px}.row-2{top:332px}.row-3{top:596px}.row-4{top:859px}
  .abs{position:absolute}
  .brand{position:absolute;font-family:var(--serif);color:var(--sage-deep);font-size:10px;letter-spacing:.3px;white-space:nowrap;display:flex;align-items:center;gap:3px}
  .brand .dot{width:5px;height:5px;border-radius:50%;background:currentColor;display:inline-block}
  .brand.top{right:17px;top:14px}
  .brand.light{color:var(--white)}
  .heading{font-family:var(--serif);color:var(--sage-deep);font-size:12.5px;letter-spacing:-.2px;white-space:nowrap}
  .heading.light{color:var(--white)}
  .body-text{font-size:4.6px;line-height:7.4px;color:var(--ink)}
  .body-text.light{color:var(--white)}
  .photo{position:absolute}
  /* cover */
  .cover{background:var(--sage)}
  .cover .brand{left:48px;top:92px;font-size:24px;color:var(--white);gap:6px}
  .cover .brand .dot{width:10px;height:10px}
  .cover .tagline{position:absolute;left:56px;top:131px;font-size:5.6px;color:var(--white)}
  /* vision */
  .vision{background:var(--cream)}
  .vision .leaf-deco{right:0;top:40px;width:170px;height:193px;background:radial-gradient(ellipse at 60% 55%,rgba(232,221,180,.7),rgba(239,238,217,0) 70%)}
  .vm{position:absolute;top:88px;width:92px}
  .vm .heading{display:flex;align-items:center;gap:3px;margin-bottom:6px}
  .vm svg{width:11px;height:11px}
  /* problem */
  .problem .left{left:0;top:0;width:207px;height:233px;background:linear-gradient(135deg,#dfe1cc,#d2d7c0)}
  .problem .forest{left:207px;top:0;width:208px;height:233px;background:radial-gradient(ellipse at 30% 20%,#8fa57a,#2f5a22 45%,#13260f 100%)}
  .block{position:absolute;left:50px;width:135px}
  .block .heading{margin-bottom:5px;display:flex;align-items:center;gap:3px}
  .block p+p{margin-top:4px}
  /* targeting */
  .target{background:var(--cream)}
  .target .panel{left:29px;top:59px;width:138px;height:148px;background:var(--sage);padding:29px 16px 0}
  .panel .lead{font-family:var(--serif);color:var(--white);font-size:10px;line-height:11px;margin-bottom:6px}
  .grid{position:absolute;left:167px;top:59px;width:221px;height:148px;display:grid;grid-template-columns:repeat(3,1fr);grid-template-rows:repeat(2,1fr)}
  .cell{position:relative}
  .cell span{position:absolute;left:5px;bottom:3px;font-family:var(--serif);color:var(--white);font-size:8px;line-height:8px}
  /* location */
  .location{background:var(--white)}
  .location .terrace{left:0;top:0;width:207px;height:233px;background:linear-gradient(160deg,#3f5e2c,#2c4a1f 55%,#3d5a2a)}
  .location .map{left:240px;top:0;width:170px;height:233px;background:radial-gradient(ellipse at 50% 55%,#4f7f38 0%,#5fa0a0 40%,rgba(255,255,255,0) 72%)}
  .location .text{position:absolute;left:31px;top:42px;width:110px}
  .location .sub{font-size:4.6px;font-weight:700;color:var(--white);margin:6px 0 5px}
  /* values */
  .values{background:linear-gradient(180deg,#b9a85c 0%,#7d8c4c 40%,#6a8a5e 70%,#6f8f66 100%)}
  .value{position:absolute;top:100px;width:62px}
  .value svg{width:20px;height:20px;margin-left:6px;margin-bottom:4px}
  .value h4{font-family:var(--serif);font-weight:400;font-size:6.8px;color:var(--white);margin-bottom:2px}
  /* founder */
  .founder{background:linear-gradient(115deg,#16300f 0%,#2f5226 45%,#6f8f4e 80%,#98ab6a 100%)}
  .founder .portrait{left:60px;top:38px;width:125px;height:195px;background:radial-gradient(ellipse at 50% 40%,#8c8b82,#4c4a44 70%,rgba(22,48,15,0) 100%)}
  .founder .name{position:absolute;left:191px;top:78px;font-family:var(--serif);color:var(--white);font-size:19px;white-space:nowrap}
  .founder .bio{position:absolute;left:191px;top:108px;width:170px}
  .founder .bio p+p{margin-top:4px}
  /* trends */
  .trends{background:var(--cream)}
  .card{position:absolute;top:58px;width:114px;height:152px}
  .card .stat{position:absolute;left:25px;top:44px;width:67px;border:.8px solid var(--white);padding:2px 3px;font-size:8px;line-height:9px;color:var(--white)}
  .card .stat b{font-weight:700}
  .card .src{position:absolute;left:3px;bottom:3px;font-size:3px;color:var(--white);text-decoration:underline}
</style>
</head>
<body>

<section class="slide cover col-l row-1">
  <div class="brand"><span class="dot"></span>THE VERDANT</div>
  <p class="tagline">The greatest quest in life is to reach one's highest potential.</p>
</section>

<section class="slide vision col-r row-1">
  <div class="abs leaf-deco" role="img" aria-label="Faint botanical leaf decoration"></div>
  <div class="brand top"><span class="dot"></span>THE VERDANT</div>
  <div class="vm" style="left:50px">
    <h3 class="heading"><svg viewBox="0 0 12 12"><circle cx="6" cy="6" r="5" fill="none" stroke="#5f7b57" stroke-width="1"/><circle cx="6" cy="6" r="2.4" fill="#5f7b57"/></svg>VISION</h3>
    <p class="body-text">Creating communities and experiences that revolutionize optimal living and evoke transformation. Empowering co-creation passion and purpose to awaken the ultimate self.</p>
  </div>
  <div class="vm" style="left:158px">
    <h3 class="heading"><svg viewBox="0 0 12 12"><path d="M1 11 L5 3 L7 7 L8.5 5 L11 11" fill="none" stroke="#5f7b57" stroke-width="1"/></svg>MISSION</h3>
    <p class="body-text">To shape conscious co-living spaces and experiences where facilitators, creatives, entrepreneurs and wanderers alike come together to reach their highest potential. Creating a sanctuary for those who crave growth, connection and self-actualization.</p>
  </div>
</section>

<section class="slide problem col-l row-2">
  <div class="photo left" role="img" aria-label="Misty jungle backdrop fading to pale sage"></div>
  <div class="photo forest" role="img" aria-label="Sunlit rainforest canopy"></div>
  <div class="brand top light"><span class="dot"></span>THE VERDANT</div>
  <div class="block" style="top:32px">
    <h3 class="heading">THE PROBLEM</h3>
    <p class="body-text">Majority of our western civilization has become disconnected from themselves, nature and others. Chasing material possessions in a concrete jungle. Loneliness and stress has become an epidemic.</p>
    <p class="body-text">People are seeking a place to live and grow in a community of like minded people that inspire and support their growth and passions.</p>
  </div>
  <div class="block" style="top:135px">
    <h3 class="heading">OUR PROMISE</h3>
    <p class="body-text">Our purpose is to create a transformative hub for change makers seeking personal development and optimal living with a desire to always drive positive change in the world. We inspire people to live a balanced lifestyle that fosters a deeper connection to themselves, others and nature. Creating an optimised way of life that covers all areas of success, health and wealth.</p>
  </div>
</section>

<section class="slide target col-r row-2">
  <div class="brand top"><span class="dot"></span>THE VERDANT</div>
  <h2 class="heading abs" style="left:32px;top:40px">WHO ARE WE TARGETING?</h2>
  <div class="abs panel">
    <p class="lead">We are seeking those who envision more depth, meaning and purpose in their lives.</p>
    <p class="body-text light" style="font-size:5px;line-height:8.5px">A collaboration of creative people that together, fuel unforgettable and life-changing experiences.</p>
  </div>
  <div class="grid">
    <div class="cell" role="img" aria-label="Portrait of a facilitator" style="background:linear-gradient(160deg,#6f8a86,#8a8f7a)"><span>Facilitators</span></div>
    <div class="cell" role="img" aria-label="Portrait of an entrepreneur" style="background:linear-gradient(160deg,#c9d2d2,#7f9aa0)"><span>Entrepreneurs</span></div>
    <div class="cell" role="img" aria-label="Photographer at sunset over hills" style="background:linear-gradient(180deg,#b48a55,#4a5f6e)"><span>Experience<br>Creators</span></div>
    <div class="cell" role="img" aria-label="Artist drawing at a desk" style="background:linear-gradient(160deg,#d8d2c6,#9b8d7e)"><span>Artists</span></div>
    <div class="cell" role="img" aria-label="Remote worker at a laptop" style="background:linear-gradient(160deg,#7f957a,#3c4a3c)"><span>Remote Workers</span></div>
    <div class="cell" role="img" aria-label="Portrait of a social impact investor" style="background:linear-gradient(160deg,#7fb4c8,#d9b89a)"><span>Social Impact<br>Investors</span></div>
  </div>
</section>

<section class="slide location col-l row-3">
  <div class="photo terrace" role="img" aria-label="Aerial view of rice terraces and palms"></div>
  <div class="photo map" role="img" aria-label="Site plan of the property along the river"></div>
  <div class="brand top"><span class="dot"></span>THE VERDANT</div>
  <div class="text">
    <h2 class="heading light">OUR LOCATION</h2>
    <p class="sub">THE PROPERTY</p>
    <p class="body-text light">Nestled in the lush jungle of Bali between Canggu and Ubud, our incredible property sits on 2.2 hectares of land with a large river that flows through. We host 10 rooms at present and soon to be 30 more, expanding our scenic space so we can co-create new ideas, projects and technology that enable a healthier lifestyle.</p>
  </div>
</section>

<section class="slide values col-r row-3" role="img" aria-label="Sunlit palm jungle and rice terraces">
  <div class="brand top light"><span class="dot"></span>THE VERDANT</div>
  <h2 class="heading light abs" style="left:32px;top:40px">VALUES</h2>
  <div class="value" style="left:32px">
    <svg viewBox="0 0 20 20" fill="none" stroke="#fff" stroke-width="1"><circle cx="10" cy="10" r="4"/><path d="M10 1v4M10 15v4M1 10h4M15 10h4M3.6 3.6l2.8 2.8M13.6 13.6l2.8 2.8M3.6 16.4l2.8-2.8M13.6 6.4l2.8-2.8"/></svg>
    <h4>Communities</h4>
    <p class="body-text light">A powerful tribe of like-minded people working on their own visions. Sparking new connections that revive &amp; thrive in wonderous co-existence.</p>
  </div>
  <div class="value" style="left:105px">
    <svg viewBox="0 0 20 20" fill="none" stroke="#fff" stroke-width="1"><path d="M10 17 C3 12 2 8 4 5 C6 3 9 4 10 6 C11 4 14 3 16 5 C18 8 17 12 10 17Z"/></svg>
    <h4>Healthy Living</h4>
    <p class="body-text light">Creating &amp; inspiring a healthy lifestyle that nurtures the resilience of both mind &amp; body with a focus on self-care.</p>
  </div>
  <div class="value" style="left:179px">
    <svg viewBox="0 0 20 20" fill="none" stroke="#fff" stroke-width="1"><path d="M10 4v14M2 5c3 1 5 2 8 2s5-1 8-2M4 8c2 .8 4 1.5 6 1.5S14 8.8 16 8"/></svg>
    <h4>Freedom</h4>
    <p class="body-text light">Freedom is everything. Without it we're bound by the chains of inner conflict. So we shape liberating spaces for everyone to feel boundless &amp; free.</p>
  </div>
  <div class="value" style="left:252px">
    <svg viewBox="0 0 20 20" fill="none" stroke="#fff" stroke-width="1"><path d="M10 19V8M10 12C6 11 4 8 5 4c3 0 5 3 5 8M10 10c3-1 6-3 6-7-3 0-6 3-6 7"/></svg>
    <h4>Growth</h4>
    <p class="body-text light">Forever working towards new heights &amp; sky high perspectives. We believe to grow on this earth is to expand: mentally, emotionally, physically &amp; spiritually.</p>
  </div>
  <div class="value" style="left:326px">
    <svg viewBox="0 0 20 20" fill="none" stroke="#fff" stroke-width="1"><path d="M2 13h14l-3-3M18 8H4l3 3"/></svg>
    <h4>Giving Back</h4>
    <p class="body-text light">Embracing the traditions of the land by supporting &amp; sourcing from local communities. Local engagement is super important to us, so a % of the total profits will go towards supporting local projects decided by our community.</p>
  </div>
</section>

<section class="slide founder col-l row-4">
  <div class="photo portrait" role="img" aria-label="Black and white portrait of the founder"></div>
  <h2 class="name">Callum Ashford</h2>
  <div class="bio">
    <p class="body-text light">After travelling for 15 years in over 75 countries, Callum has chosen to settle down in Bali to create and build The Verdant. He has 13 years of experience running a well-established travel company that comprises many different lifestyle brands including a co-living company and a small hotel in Thailand. Generating 8 figures of revenue over the last decade.</p>
    <p class="body-text light">Now he is shifting his focus to create a more balanced lifestyle fueled by his passion for personal development and positive impact in the world.</p>
  </div>
</section>

<section class="slide trends col-r row-4">
  <div class="brand top"><span class="dot"></span>THE VERDANT</div>
  <h2 class="heading abs" style="left:32px;top:40px">MARKET TRENDS</h2>
  <div class="card" style="left:33px;background:linear-gradient(160deg,#d8cfc2,#a58e7a)" role="img" aria-label="People sharing a meal in a co-living kitchen">
    <p class="stat">Co-Living to be growing from <b>6.7 Billion to 14 Billion</b> in 2025</p>
    <p class="src">Source: co-living market report</p>
  </div>
  <div class="card" style="left:155px;background:linear-gradient(160deg,#5d8a4a,#24451c)" role="img" aria-label="Jungle swing over rainforest">
    <p class="stat">Experience Economy will be worth <b>12 Billion</b> by 2023</p>
    <p class="src">Source: experience economy study</p>
  </div>
  <div class="card" style="left:276px;background:linear-gradient(170deg,#b7c7c4,#7f9290)" role="img" aria-label="Woman meditating on a wooden deck">
    <p class="stat">Personal Development to be growing from <b>9.9 Billion to 13 Billion</b> by 2022</p>
    <p class="src">Source: wellness industry outlook</p>
  </div>
</section>

</body>
</html>
```